Professional Lighting Providers - Web Design

We need a web design to showcase our ability to provide lighting design and equipment to those who are in need of lighting equipment.

Our 4 markets are:
Broadcasting - Public and Commercial
Education - ISD wide, and private schools
Government - National News, Chamber videos, Press Releases
Religious - Sermon Recording, etc.

We provide lighting products, design consultations(how lights are setup and such), and custom light work.

We want the home page to be setup in a way that someone in one of the 4 markets can drill down into the site. Meaning they are greeted on the home page with 4 large icons or pictures for each market and then they can go farther into the site. We also want a top navigation to be preset so people who are just looking for lighting can also browse our products.

Logo colors are not as they appear on our current website.
#383388 is our current logo color, please also see attachment of logo. In addition, we are just "Clear Beam - Lighting Systems". We dropped the RZ7 out of our name so please don't use it in the concept.

Our Current Site is http://rz7-example.com/index.asp.
We don't have set colors but we know we do not want reds or yellows.

The design should be simple, not cluttered, and not artsy, not fun, but very serious.

Requirements
Must have
• Image banner/slider at the top that slides our 4 products.
Also need to have a form on the home page that will convert visitors to subscribers for a newsletter. Also on every page we want a form were people can send an email off to us asking questions.

```html
<!DOCTYPE html>
<html lang="en">
<head>
<meta charset="utf-8">
<title>Clear Beam - Lighting Systems</title>
<link href="https://fonts.googleapis.com/css2?family=Ubuntu:wght@300;400;500;700&family=Open+Sans:wght@400;600&family=Damion&display=swap" rel="stylesheet">
<style>
:root{
  --navy:#0b2a5e;
  --brand:#383388;
  --cyan:#14abdc;
  --cyan-dark:#0a8fc0;
  --frame:#2b2b2b;
  --heading:#0d3a7a;
  --green:#4a8a2a;
  --link:#2a7fc9;
  --muted:#777;
  --panel:#f1f1f1;
  --line:#cfcfcf;
}
*{box-sizing:border-box;margin:0;padding:0}
html,body{width:1108px;height:1200px;overflow:hidden;background:#fff}
.page{position:relative;width:1200px;height:1300px;transform:scale(.92334);transform-origin:0 0;font-family:Arial,Helvetica,sans-serif;color:#222}
.abs{position:absolute}
.topbar{left:0;top:0;width:1200px;height:6px;background:var(--navy)}
.brand{left:128px;top:30px;display:flex;align-items:center;gap:12px}
.brand-mark{width:40px;height:40px;background:var(--brand);border-radius:6px}
.brand-name{font-family:Ubuntu,sans-serif;font-weight:500;color:var(--brand);font-size:22px;line-height:26px}
.nav{left:401px;top:35px;width:656px;height:54px;border-radius:3px;background:linear-gradient(#3cc6ee,#0aa0d2);border:1px solid #0a94c4;display:flex;align-items:center;padding-left:12px}
.nav a{flex:none;white-space:nowrap;text-align:center;font-size:13px;font-weight:bold;color:#fff;text-decoration:none;border-left:1px solid rgba(255,255,255,.35);line-height:26px;text-shadow:0 1px 0 rgba(0,0,0,.2)}
.nav a.home{width:72px;background:#fff;color:#222;border:2px solid #9ad9ef;line-height:29px;text-shadow:none}
.nav a.home+a{border-left:none}
.slider{left:115px;top:126px;width:968px;height:415px;background:var(--frame);border-radius:14px}
.slide{left:134px;top:141px;width:929px;height:382px;border-radius:10px;background:linear-gradient(100deg,#8d9be0 0%,#6d7fd3 28%,#2b3fa6 42%,#233594 70%,#2d3f9c 100%)}
.caption{left:134px;top:141px;width:436px;height:74px;border-top-left-radius:10px;background:rgba(206,210,245,.78);font-family:Ubuntu,sans-serif;font-weight:300;font-size:27px;color:#333;padding:22px 0 0 14px;white-space:nowrap}
.dot{top:493px;width:23px;height:23px;border-radius:50%;background:radial-gradient(circle at 40% 35%,#fff,#d6d6d6);border:1px solid #bbb}
.dot.on{background:radial-gradient(circle at 40% 35%,#3ad0f5,#0a9ccc);border-color:#0a8fc0}
.shadow{left:180px;top:540px;width:880px;height:40px;border-radius:50%;background:radial-gradient(ellipse at 50% 0%,rgba(0,0,0,.35),rgba(0,0,0,0) 70%)}
.market{top:585px;width:205px}
.market h2{font-family:Ubuntu,sans-serif;font-weight:400;font-size:18px;color:#222;margin:0 0 6px 4px;white-space:nowrap}
.market .photo{width:203px;height:117px;border:3px solid #3cc8ec;border-bottom:5px solid #1d3a55;border-radius:4px}
.market p{font-family:"Open Sans",sans-serif;font-size:11.5px;line-height:20px;color:var(--muted);margin:12px 0 0 5px;width:200px}
.btn{display:block;width:93px;height:30px;background:linear-gradient(#25b9e6,#0a9fd2);border:1px solid #0a8fc0;color:#fff;font-family:Ubuntu,sans-serif;font-size:13px;text-align:center;line-height:28px;text-decoration:none;white-space:nowrap}
.rule{left:128px;top:897px;width:940px;height:1px;background:#c8c8c8}
.packages{left:144px;top:930px;width:272px}
h3{font-family:Ubuntu,sans-serif;font-weight:500;font-size:19.5px;color:var(--heading);white-space:nowrap}
.sub{font-family:Ubuntu,sans-serif;font-size:12.5px;color:var(--green);margin-top:2px}
.packages p{font-size:12.5px;line-height:16.5px;margin-top:18px}
.packages ul{list-style:none;margin-top:14px}
.packages li{font-size:12.5px;font-weight:bold;color:var(--link);height:21px;display:flex;align-items:center;gap:8px}
.packages li svg{flex:none}
.reviews{left:426px;top:914px;width:267px;height:263px;background:var(--panel);border-radius:6px;padding:16px 11px}
.reviews h4{font-family:Ubuntu,sans-serif;font-weight:400;font-size:12.5px;color:var(--green);margin-top:16px}
.reviews p{font-size:11px;line-height:13px;margin-top:4px;padding-left:1px;padding-right:10px}
.reviews .lead{margin-top:10px;padding-bottom:14px;border-bottom:1px dotted #999}
.reviews .mid{padding-bottom:14px;border-bottom:1px dotted #999}
.reviews .last{line-height:16.5px}
.newsletter{left:721px;top:914px;width:340px;height:258px;border:1px solid var(--line);border-radius:8px}
.newsletter .title{position:absolute;left:16px;top:6px;font-family:Damion,cursive;font-size:31px;color:#1a4aa0}
.newsletter .intro{position:absolute;left:21px;top:51px;font-size:12px;color:#666;white-space:nowrap}
.newsletter label{position:absolute;left:26px;font-size:12px;color:#555}
.newsletter .field{position:absolute;left:87px;width:231px;height:40px;border:1px solid #bbb;border-radius:4px;background:#fff}
.subscribe{position:absolute;left:84px;top:204px;width:126px;height:40px;border-radius:4px;background:linear-gradient(#ffd21a,#f5ab00);border-bottom:3px solid #e0900a;font-size:14px;color:#222;text-align:center;line-height:38px}
.footer{left:0;top:1234px;width:1200px;height:66px;background:linear-gradient(#5a5a5a,#2c2c2c);border-top:2px solid #888;text-align:center;font-family:"Open Sans",sans-serif;color:#fff}
.footer nav{margin-top:16px;font-size:11px}
.footer nav a{color:#fff;text-decoration:none;margin:0 15px}
.footer small{display:block;font-size:11px;margin-top:5px}
</style>
</head>
<body>
<div class="page">
  <div class="abs topbar"></div>

  <header>
    <div class="abs brand">
      <span class="brand-mark"></span>
      <span class="brand-name">Clear Beam<br>Lighting Systems</span>
    </div>
    <nav class="abs nav">
      <a class="home" href="#">Home</a>
      <a href="#" style="width:104px">About Us</a>
      <a href="#" style="width:105px">Products</a>
      <a href="#" style="width:98px">Services</a>
      <a href="#" style="width:150px">Lighting Designs</a>
      <a href="#" style="width:113px">Contact Us</a>
    </nav>
  </header>

  <section>
    <div class="abs slider"></div>
    <div class="abs slide" role="img" aria-label="Illuminated blue glass office tower at dusk"></div>
    <div class="abs caption">Real sloutions to studio lightning</div>
    <span class="abs dot on" style="left:146px"></span>
    <span class="abs dot" style="left:175px"></span>
    <span class="abs dot" style="left:205px"></span>
    <span class="abs dot" style="left:236px"></span>
    <div class="abs shadow"></div>
  </section>

  <section>
    <div class="abs market" style="left:146px">
      <h2>Broadcasting</h2>
      <div class="photo" role="img" aria-label="Radio host at a broadcast microphone" style="background:linear-gradient(135deg,#6a7482,#c9b8a8 60%,#3b3f48)"></div>
      <p>Lorem Ipsum is simply dummy text of the printing and typesetting industry. Lorem Ipsum has been the industry's standard dummy text ever</p>
      <a class="btn" href="#" style="margin:11px 0 0 47px">Read more</a>
    </div>
    <div class="abs market" style="left:370px">
      <h2>Education</h2>
      <div class="photo" role="img" aria-label="Empty classroom with desks under ceiling lights" style="background:linear-gradient(#e6e4dc,#a9a89c 60%,#8a7a60)"></div>
      <p>Lorem Ipsum is simply dummy text of the printing and typesetting industry. Lorem Ipsum has been the industry's standard dummy text ever</p>
      <a class="btn" href="#" style="margin:11px 0 0 53px">Read more</a>
    </div>
    <div class="abs market" style="left:593px">
      <h2>National News</h2>
      <div class="photo" role="img" aria-label="Press conference audience with cameras" style="background:linear-gradient(#d9b891,#8a6a50 55%,#3d3430)"></div>
      <p>Lorem Ipsum is simply dummy text of the printing and typesetting industry. Lorem Ipsum has been the industry's standard dummy text ever</p>
      <a class="btn" href="#" style="margin:11px 0 0 64px">Read more</a>
    </div>
    <div class="abs market" style="left:817px">
      <h2>Sermon Recording</h2>
      <div class="photo" role="img" aria-label="Studio microphone over a blue sound wave" style="background:linear-gradient(90deg,#062438,#0f6a94 55%,#0a2a40)"></div>
      <p>Lorem Ipsum is simply dummy text of the printing and typesetting industry. Lorem Ipsum has been the industry's standard dummy text ever</p>
      <a class="btn" href="#" style="margin:11px 0 0 58px">Read more</a>
    </div>
  </section>

  <div class="abs rule"></div>

  <section class="abs packages">
    <h3>Best Lighting Packages</h3>
    <div class="sub">Deals that you can't refuse</div>
    <p>Lorem ipsum dolor sit amet, consectetur adipis-icing elit, sed do eiusmod tempor incididunt ut labore et dolore magna aliqua. Ut enim ad minim veniam.</p>
    <ul>
      <li><svg width="7" height="10" viewBox="0 0 7 10"><path d="M1 1l4 4-4 4" stroke="#0d3a7a" stroke-width="2" fill="none"/></svg>Lorem ipsum dolor sit</li>
      <li><svg width="7" height="10" viewBox="0 0 7 10"><path d="M1 1l4 4-4 4" stroke="#0d3a7a" stroke-width="2" fill="none"/></svg>Amet, consectetur</li>
      <li><svg width="7" height="10" viewBox="0 0 7 10"><path d="M1 1l4 4-4 4" stroke="#0d3a7a" stroke-width="2" fill="none"/></svg>Adipisicing elit, sed</li>
      <li><svg width="7" height="10" viewBox="0 0 7 10"><path d="M1 1l4 4-4 4" stroke="#0d3a7a" stroke-width="2" fill="none"/></svg>Fo eiusmod tempor</li>
      <li><svg width="7" height="10" viewBox="0 0 7 10"><path d="M1 1l4 4-4 4" stroke="#0d3a7a" stroke-width="2" fill="none"/></svg>Klncididunt ut labore</li>
    </ul>
  </section>

  <section class="abs reviews">
    <h3>Latest Project &amp; Reviews</h3>
    <p class="lead">Lorem ipsum dolor sit amet, consectetur adipisicing elit, sed do eiusmod tempor incididunt ut labore et dolore magna aliqua.</p>
    <h4>Insight View</h4>
    <p class="mid">Lorem ipsum dolor sit amet, consectetur adipis-icing elit, sed do eiusmod tempor incididunt ut</p>
    <h4>Broad Selection</h4>
    <p class="last">consectetur adipisicing elit, sed do eiusmod tempor incididunt ut labore et dolore magna aliqua. Ut enim ad minim veniam.</p>
  </section>

  <section class="abs newsletter">
    <div class="title">Newsletter</div>
    <div class="intro">Join our bi-monthly email newsletter for the latest offer</div>
    <label style="top:115px">Name:</label>
    <div class="field" style="top:100px"></div>
    <label style="top:164px">E-mail:</label>
    <div class="field" style="top:150px"></div>
    <div class="subscribe">Subscribe</div>
  </section>

  <footer class="abs footer">
    <nav><a href="#">Home</a><a href="#">About Us</a><a href="#">Products</a><a href="#">Latest News</a><a href="#">Contact Us</a></nav>
    <small>Copyright 2012. All Rights Reserved</small>
  </footer>
</div>
</body>
</html>
```